Falcrest security business card

Looking for a business card for my security company

Target Market(s)

Security

Industry/Entity Type

Security

Contact Information for Business Card

Name - Gil Marston. Title - General manager - direct 314 862.4490 website www. falcrestsecurityservices.example email - gil@ falcrestsecurityservices.example

Requirements
Must have
• Logo attached

```html
<!DOCTYPE html>
<html lang="en">
<head>
<meta charset="utf-8">
<title>Falcrest Security Services – Business Card</title>
<link rel="stylesheet" href="https://fonts.googleapis.com/css2?family=Roboto+Condensed:wght@400;700&family=Oswald:wght@700&display=swap">
<style>
  :root {
    --ink: #000000;
    --night: #020202;
    --gold-light: #e2bf57;
    --gold-mid: #c8973a;
    --gold-deep: #9d6516;
    --gold-line: #b8862c;
    --brand-gold: #d6ad4a;
  }
  * { margin: 0; padding: 0; box-sizing: border-box; }
  html, body {
    width: 1200px;
    height: 686px;
    overflow: hidden;
    background: var(--night);
  }
  .card {
    position: relative;
    width: 1200px;
    height: 686px;
    background: var(--night);
    overflow: hidden;
  }
  .brand {
    position: absolute;
    left: 0;
    top: 0;
    width: 1200px;
    height: 414px;
    display: flex;
    align-items: center;
    justify-content: center;
  }
  .brand-name {
    font-family: "Roboto Condensed", sans-serif;
    font-weight: 700;
    font-size: 96px;
    letter-spacing: 6px;
    color: var(--brand-gold);
    text-transform: uppercase;
    line-height: 1;
  }
  .rule {
    position: absolute;
    left: 0;
    top: 416px;
    width: 1200px;
    height: 5px;
    background: var(--gold-line);
  }
  .contact-band {
    position: absolute;
    left: 0;
    top: 430px;
    width: 1200px;
    height: 256px;
    background:
      radial-gradient(ellipse 520px 260px at 600px 150px, var(--gold-light) 0%, var(--gold-mid) 55%, var(--gold-deep) 100%);
  }
  .person {
    position: absolute;
    left: 100px;
    top: 84px;
    width: 340px;
    text-align: center;
    color: var(--ink);
  }
  .person-name {
    font-family: "Oswald", sans-serif;
    font-weight: 700;
    font-size: 44px;
    line-height: 1.05;
    letter-spacing: -0.5px;
  }
  .person-title {
    font-family: "Roboto Condensed", sans-serif;
    font-weight: 400;
    font-size: 27px;
    line-height: 1.3;
    text-transform: uppercase;
  }
  .contact-list {
    position: absolute;
    left: 496px;
    top: 40px;
    list-style: none;
  }
  .contact-item {
    display: flex;
    align-items: center;
    height: 63px;
    color: var(--ink);
    font-family: "Roboto Condensed", sans-serif;
    font-weight: 400;
    font-size: 37px;
  }
  .contact-icon {
    width: 46px;
    height: 42px;
    margin-right: 16px;
    flex: none;
  }
</style>
</head>
<body>
<div class="card">
  <header class="brand">
    <span class="brand-name">Falcrest</span>
  </header>

  <div class="rule"></div>

  <section class="contact-band">
    <div class="person">
      <div class="person-name">Gil Marston</div>
      <div class="person-title">General Manager</div>
    </div>

    <ul class="contact-list">
      <li class="contact-item">
        <svg class="contact-icon" viewBox="0 0 46 42" fill="none" stroke="#000" stroke-width="2.2" stroke-linejoin="round">
          <path d="M10 5 l6 -1 l4 9 l-4 3 q3 8 10 12 l3 -4 l9 4 l-1 6 q-3 4 -9 2 q-15 -6 -20 -22 q-1 -6 2 -9 z"/>
          <path d="M28 6 q8 2 10 10" stroke-linecap="round"/>
          <path d="M27 12 q4 1 5 5" stroke-linecap="round"/>
        </svg>
        <span>314 862 4490</span>
      </li>
      <li class="contact-item">
        <svg class="contact-icon" viewBox="0 0 46 42" fill="none" stroke="#000" stroke-width="2.4" stroke-linejoin="round">
          <rect x="4" y="9" width="38" height="25"/>
          <path d="M4 9 l19 15 l19 -15"/>
        </svg>
        <span>gil@falcrestsecurityservices.example</span>
      </li>
      <li class="contact-item">
        <svg class="contact-icon" viewBox="0 0 46 42" fill="none" stroke="#000" stroke-width="2.2">
          <circle cx="23" cy="21" r="18"/>
          <ellipse cx="23" cy="21" rx="8" ry="18"/>
          <line x1="5" y1="21" x2="41" y2="21"/>
          <path d="M8 12 h30 M8 30 h30"/>
        </svg>
        <span>www.falcrestsecurityservices.example</span>
      </li>
    </ul>
  </section>
</div>
</body>
</html>
```